Business Card Design Project

The logo I included in my order was a previous image that we've used for shirts, signs, magnets, etc. We've decided to go back to that logo, with some updates.
We need to add "Inc." after "Brindel Roofing,"
Also, I need the logo with a transparent background so that I can use it on other projects.

The business cards will be the first item I order with the new logo. The employee's info is:
Derek Pallow
Sales Manager
484-611-3907
dpallow@brindelroofinginc.example

Also, I want a "Find us on Linkora" icon on the card, along with our web address, www.brindelroofinginc.example.

Any questions, please email or call me:
norabrindel@mailbox.example
484-290-6153

Reason: This is the first time I've tried Pixel Forum.

My timetable changed and I need to select a design by the end of the work day, 6 hours from now.Thanks so much for all of the super designs.

Target Market(s)

Homeowners

Industry/Entity Type

Business

Font styles to use
Serif

Requirements
Must have
• Transparent background
Similar to logo in photo I sent you

```html
<!DOCTYPE html>
<html lang="en">
<head>
<meta charset="utf-8">
<title>Brindel Roofing Inc. – Business Card</title>
<link href="https://fonts.googleapis.com/css2?family=Marcellus+SC&family=Encode+Sans+Condensed:wght@300;600&display=swap" rel="stylesheet">
<style>
  :root {
    --page-bg: #2b2622;
    --card-light: #3b3b3b;
    --card-dark: #1b1b1b;
    --brand-slate: #a6b3b3;
    --band: #98a6a6;
    --text-light: #e9eded;
    --text-muted: #8c9494;
    --strip: #202020;
  }
  * { margin: 0; padding: 0; box-sizing: border-box; }
  html, body {
    width: 1200px;
    height: 1000px;
    overflow: hidden;
    background: var(--page-bg);
  }
  .business-card {
    position: absolute;
    left: 120px;
    top: 226px;
    width: 958px;
    height: 547px;
    background: radial-gradient(ellipse 70% 80% at 50% 35%, var(--card-light), var(--card-dark));
    box-shadow: 0 10px 30px rgba(0,0,0,0.5);
    overflow: hidden;
  }
  .brand-name {
    position: absolute;
    top: 195px;
    left: 0;
    width: 100%;
    text-align: center;
    font-family: "Marcellus SC", serif;
    font-size: 58px;
    line-height: 1;
    color: var(--brand-slate);
  }
  .employee-name {
    position: absolute;
    top: 300px;
    left: 0;
    width: 100%;
    text-align: center;
    font-family: "Marcellus SC", serif;
    font-size: 44px;
    line-height: 1;
    color: var(--text-light);
  }
  .employee-title {
    position: absolute;
    top: 345px;
    left: 0;
    width: 100%;
    text-align: center;
    font-family: "Encode Sans Condensed", sans-serif;
    font-weight: 300;
    font-size: 15px;
    color: var(--text-muted);
  }
  .employee-contact {
    position: absolute;
    top: 378px;
    left: 0;
    width: 100%;
    text-align: center;
    font-family: "Encode Sans Condensed", sans-serif;
    font-weight: 300;
    font-size: 20px;
    color: #c9cfcf;
    word-spacing: 1px;
  }
  .employee-contact .divider { margin: 0 8px; }
  .info-band {
    position: absolute;
    top: 420px;
    left: 0;
    width: 100%;
    height: 68px;
    background: var(--band);
    display: flex;
    align-items: center;
    justify-content: center;
    font-family: "Marcellus SC", serif;
    font-size: 36px;
    color: #ffffff;
  }
  .info-band .divider { margin: 0 16px; }
  .social-strip {
    position: absolute;
    top: 488px;
    left: 0;
    width: 100%;
    height: 59px;
    background: var(--strip);
    display: flex;
    align-items: center;
    justify-content: center;
    gap: 8px;
    font-family: "Encode Sans Condensed", sans-serif;
    font-weight: 600;
    font-size: 16px;
    color: #ffffff;
  }
  .social-strip .dot {
    width: 12px;
    height: 12px;
    border-radius: 50%;
    background: #ffffff;
  }
</style>
</head>
<body>
  <div class="business-card">
    <div class="brand-name">Brindel Roofing Inc.</div>
    <div class="employee-name">Derek Pallow</div>
    <div class="employee-title">sales manager</div>
    <div class="employee-contact">cell: (484) 611-3907<span class="divider">|</span>email: dpallow@brindelroofinginc.example</div>
    <div class="info-band">(610) 738-2145<span class="divider">|</span>BrindelRoofingInc.example</div>
    <div class="social-strip"><span class="dot"></span><span>Find us on Linkora</span></div>
  </div>
</body>
</html>
```